Post storm repair flyer

looking for an eye catching 6x9 postcard to send out to single family home owners advertising a "Post Storm Repair Special" explaining that after the recent hurricanes its very important to have your roof checked and any repairs fixed right away before they become a bigger more costly problem and that even though your home wasn't directly hit by the storm the high wind gust could've cause unseen damage.
offer $200 off any repair *some rules may apply
Lark Roofing
888.417.LARK
www.LarkRoofing.example

Roofing

```html
<!DOCTYPE html>
<html lang="en">
<head>
<meta charset="utf-8">
<title>Lark Roofing – Post-Storm Repair Special Postcard</title>
<link href="https://fonts.googleapis.com/css2?family=Anton&family=Oswald:wght@400;500;600&family=Montserrat:wght@500;700;800&display=swap" rel="stylesheet">
<style>
  :root{
    --honey:#e8b021;
    --ink:#000000;
    --charcoal:#333036;
    --paper:#ffffff;
    --backdrop:#d1d2d4;
  }
  *{margin:0;padding:0;box-sizing:border-box}
  html,body{width:1073px;height:1200px;overflow:hidden;background:var(--backdrop)}
  .sheet{position:relative;width:1073px;height:1200px}
  .card{position:absolute;left:145px;width:784px;height:522px;overflow:hidden;box-shadow:2px 3px 6px rgba(0,0,0,.35)}
  .card--front{top:53px;background:var(--honey)}
  .card--back{top:610px;background:var(--paper)}
  .abs{position:absolute}

  /* front */
  .storm-photo{left:0;top:0;width:784px;height:395px}
  .headline{left:35px;top:0;width:440px;height:320px;color:var(--ink);font-weight:normal}
  .headline__line{position:absolute;left:0;display:block;height:88px;line-height:88px;white-space:nowrap;transform-origin:left}
  .headline__light{top:40px;font-family:"Oswald",sans-serif;font-weight:400;font-size:100px;letter-spacing:-2px;transform:scaleX(.81)}
  .headline__bold{font-family:"Anton",sans-serif;font-size:90px;letter-spacing:-1px;transform:scaleX(1.09)}
  .headline__bold--repair{top:135px}
  .headline__bold--special{top:224px}
  .offer-bar{left:0;top:318px;width:470px;height:50px;background:var(--ink);color:var(--paper);font-family:"Montserrat",sans-serif;font-weight:700;font-size:13.6px;line-height:18px;padding:8px 0 0 38px;letter-spacing:.2px}
  .front-brand{left:600px;top:105px;width:168px;text-align:center;font-family:"Montserrat",sans-serif;font-weight:500;font-size:14px;color:var(--honey);letter-spacing:.5px}
  .footer-strip{left:0;top:395px;width:478px;height:127px;background:var(--charcoal)}
  .footer-contact{left:478px;top:395px;width:306px;height:127px;background:var(--ink);text-align:center;padding-top:32px}
  .deal-amount{font-family:"Anton",sans-serif;color:var(--honey);line-height:1}
  .deal-caption{font-family:"Oswald",sans-serif;font-weight:600;line-height:1;letter-spacing:-.5px}
  .front-deal{left:39px;top:14px}
  .front-deal .deal-amount{font-size:76px;letter-spacing:-2px;transform:scaleX(.9);transform-origin:left}
  .front-deal .deal-caption{color:var(--paper);font-size:27px;margin-top:2px;transform:scaleX(.85);transform-origin:left}
  .divider{left:203px;top:14px;height:96px;border-left:1.5px dashed var(--paper)}
  .front-copy{left:220px;top:27px;width:250px;font-family:"Montserrat",sans-serif;font-weight:500;font-size:14px;line-height:17.5px;color:var(--paper)}
  .phone{font-family:"Montserrat",sans-serif;font-weight:800;color:var(--honey);letter-spacing:-.5px;line-height:1}
  .web{font-family:"Montserrat",sans-serif;font-weight:500;color:var(--paper);line-height:1}
  .footer-contact .phone{font-size:32px}
  .footer-contact .web{font-size:19px;margin-top:8px}

  /* back */
  .back-photo{left:0;top:0;width:380px;height:323px}
  .back-brand{left:0;top:130px;width:380px;text-align:center;font-family:"Montserrat",sans-serif;font-weight:500;font-size:14px;color:var(--ink);letter-spacing:.5px}
  .back-copy{left:0;top:180px;width:386px;text-align:center;font-family:"Montserrat",sans-serif;font-weight:500;font-size:20px;line-height:26.5px;color:var(--ink)}
  .back-deal{left:0;top:323px;width:380px;height:97px;background:var(--paper)}
  .back-deal .deal-amount{position:absolute;left:42px;top:8px;font-size:92px;letter-spacing:-2px;transform:scaleX(.88);transform-origin:left}
  .back-deal .deal-caption{position:absolute;left:210px;top:14px;color:var(--ink);font-size:40px;line-height:38px;transform:scaleX(.85);transform-origin:left}
  .back-contact{left:0;top:420px;width:380px;height:102px;background:var(--ink);padding:17px 0 0 42px}
  .back-contact .phone{font-size:33px}
  .back-contact .web{font-size:19px;margin-top:8px}
  .stamp-box{left:614px;top:41px;width:132px;height:147px;border:1px solid #333}
  .address-line{left:392px;width:277px;border-top:1px solid #555}
</style>
</head>
<body>
<div class="sheet">

  <section class="card card--front">
    <svg class="abs storm-photo" viewBox="0 0 784 395" role="img" aria-label="Photo of lightning over a tiled roof during a night storm">
      <defs>
        <linearGradient id="stormSky" x1="0" y1="0" x2="0" y2="1">
          <stop offset="0" stop-color="#3a3140"/>
          <stop offset=".4" stop-color="#6b5670"/>
          <stop offset=".7" stop-color="#4a3a3c"/>
          <stop offset="1" stop-color="#5a3a32"/>
        </linearGradient>
      </defs>
      <polygon points="377,0 784,0 784,395 368,395 470,292 368,192 466,90" fill="url(#stormSky)"/>
    </svg>

    <h1 class="abs headline">
      <span class="headline__line headline__light">POST-STORM</span>
      <span class="headline__line headline__bold headline__bold--repair">REPAIR</span>
      <span class="headline__line headline__bold headline__bold--special">SPECIAL!</span>
    </h1>

    <p class="abs offer-bar">OFFER INCLUDES A FREE INSPECTION AND<br>$200 OFF ANY QUALIFYING REPAIR.</p>

    <p class="abs front-brand">LARK ROOFING</p>

    <div class="abs footer-strip">
      <div class="abs front-deal">
        <div class="deal-amount">$200</div>
        <div class="deal-caption">OFF ANY REPAIR</div>
      </div>
      <div class="abs divider"></div>
      <p class="abs front-copy">Recent storms can cause hidden damage to your roof. Don't wait until it's too late—get a professional inspection today!</p>
    </div>

    <div class="abs footer-contact">
      <div class="phone">888.417.LARK</div>
      <div class="web">www.LarkRoofing.example</div>
    </div>
  </section>

  <section class="card card--back">
    <svg class="abs back-photo" viewBox="0 0 380 323" role="img" aria-label="Honey-tinted photo of a storm-damaged house roof">
      <defs>
        <linearGradient id="honeyWash" x1="0" y1="0" x2="1" y2="1">
          <stop offset="0" stop-color="#e9b534"/>
          <stop offset="1" stop-color="#dca830"/>
        </linearGradient>
      </defs>
      <rect width="380" height="323" fill="url(#honeyWash)"/>
    </svg>

    <p class="abs back-brand">LARK ROOFING</p>
    <p class="abs back-copy">Protect your home and avoid<br>costly repairs by addressing<br>storm damage early. Our<br>expert team is ready to help!</p>

    <div class="abs back-deal">
      <div class="deal-amount">$200</div>
      <div class="deal-caption">OFF ANY<br>REPAIR</div>
    </div>

    <div class="abs back-contact">
      <div class="phone">888.417.LARK</div>
      <div class="web">www.LarkRoofing.example</div>
    </div>

    <div class="abs stamp-box"></div>
    <div class="abs address-line" style="top:323px"></div>
    <div class="abs address-line" style="top:370px"></div>
    <div class="abs address-line" style="top:416px"></div>
    <div class="abs address-line" style="top:463px"></div>
  </section>

</div>
</body>
</html>
```